National Virtual accounting firm needs website designed

I need a wordpress website design for a national virtual accounting firm. I will upload my business card, logo, and postcards that I have had designed and followed the same style. I want a similar style to be followed so I can keep the running theme similar.

Services include:

Tax Services:
Tax preparation and planning services for Individuals, businesses, estates, and nonprofits
Full Service Payroll for Businesses
QVT Audit Representation

Consulting:
Entity Selection & Restructuring
Financial Projections & Forecasts
Retirement Planning
IPO Readiness

Accounting:
Bookkeeping
Reviews and Compilations
Payroll Services

Other Services:
CFO Services
Compliance Services
Controller Services
Software Implementations for Tenvolk, Brombalt, and Plovena.

Target Market(s)

small to medium size businesses, and individuals

Industry/Entity Type

accounting firms

Font styles to use
Sans Serif

Colors
59FF00
82FF00
B8FF75
E3FFCB
F4FFEA

Requirements
Must have
• Color schematics from the logo and post cards/business cards

```html
<!DOCTYPE html>
<html lang="en">
<head>
<meta charset="utf-8">
<title>Velora – Business Advisors &amp; Consultants</title>
<link href="https://fonts.googleapis.com/css2?family=Alfa+Slab+One&family=Poppins:wght@400;500;600;700&family=Rajdhani:wght@600;700&family=Roboto+Slab:wght@500;600;700&display=swap" rel="stylesheet">
<style>
:root{
  --green:#5cb833;
  --green-dark:#3f9a1e;
  --lime:#8fd21f;
  --lime-bright:#b8ff75;
  --mint:#dcf0c8;
  --mint-soft:#eaf7dc;
  --yellow:#ffc928;
  --ink:#111111;
  --text:#2b2b2b;
  --muted:#666666;
  --white:#ffffff;
  --footer:#0e0f0d;
}
*{margin:0;padding:0;box-sizing:border-box}
html,body{width:1200px;height:4129px;overflow:hidden;background:var(--white)}
body{font-family:'Poppins',sans-serif;color:var(--text)}
.page{position:relative;width:1200px;height:4129px;overflow:hidden}
.abs{position:absolute}

/* header */
.logo{position:absolute;display:flex;align-items:center;gap:10px}
.logo-mark{width:34px;height:34px;border-radius:50%;background:var(--yellow)}
.logo-name{font-family:'Alfa Slab One',serif;color:var(--white);font-size:34px;letter-spacing:1px}
.nav{position:absolute;top:38px;left:548px;display:flex;gap:36px;font-size:14px;font-weight:600;color:var(--white)}
.nav .active{color:var(--yellow);border-bottom:2px solid var(--yellow);padding-bottom:3px}
.call-btn{position:absolute;left:980px;top:32px;width:130px;height:36px;background:var(--yellow);border-radius:3px;display:flex;align-items:center;justify-content:center;gap:8px;font-size:15px;font-weight:600;color:var(--ink)}

/* hero */
.hero-card{position:absolute;left:90px;top:218px;width:380px;height:380px;border-radius:50%;background:var(--white);text-align:center;padding-top:76px}
.hero-ring{position:absolute;left:72px;top:200px;width:416px;height:416px;border-radius:50%;border:3px dotted var(--lime)}
.hero-kicker{font-family:'Rajdhani',sans-serif;font-weight:700;color:var(--green);font-size:36px;line-height:1}
.hero-title{font-family:'Rajdhani',sans-serif;font-weight:700;color:var(--ink);font-size:52px;line-height:1.05;margin-top:6px}
.hero-sub{font-size:19px;font-weight:600;color:var(--ink);line-height:1.35;margin-top:14px}
.hero-sub span{color:var(--green)}
.consult-btn{position:absolute;left:398px;top:492px;width:148px;height:148px;border-radius:50%;background:var(--green);color:var(--white);font-size:15px;font-weight:600;text-align:center;display:flex;align-items:center;justify-content:center;line-height:1.45}

/* section headings */
.section-title{position:absolute;font-family:'Alfa Slab One',serif;color:var(--ink);font-size:31px;letter-spacing:1px;text-align:center}
.section-title svg{display:block;margin:2px auto 0}

/* about */
.about-lead{position:absolute;left:88px;top:922px;width:440px;font-size:16px;font-weight:600;color:var(--ink);line-height:1.35}
.about-body{position:absolute;left:88px;width:460px;font-size:14.5px;line-height:1.5;color:var(--text)}
.btn-yellow{position:absolute;background:var(--yellow);color:var(--ink);font-size:15px;font-weight:600;display:flex;align-items:center;justify-content:center;border-radius:2px}
.feature{position:absolute;width:160px;text-align:center;font-size:18px;font-weight:500;color:var(--ink)}
.feature-icon{width:88px;height:88px;border-radius:50%;background:var(--green);margin:0 auto 12px;display:flex;align-items:center;justify-content:center;box-shadow:0 0 0 4px #e5f4d7}

/* services */
.service-card{position:absolute;top:1684px;width:237px;height:251px;background:var(--white);border-radius:14px;border-bottom:3px solid var(--green);text-align:center;padding-top:34px;box-shadow:0 4px 10px rgba(0,0,0,.06)}
.service-card.featured{background:var(--green);color:var(--white)}
.service-icon{width:70px;height:52px;margin:0 auto 14px;position:relative}
.service-name{font-family:'Roboto Slab',serif;font-weight:600;font-size:17px;color:var(--green);margin-bottom:10px}
.service-list{font-size:13px;line-height:1.35;color:var(--muted);height:76px}
.service-link{font-family:'Roboto Slab',serif;font-size:11px;font-weight:700;color:var(--green);margin-top:14px;letter-spacing:.5px}
.featured .service-name,.featured .service-list,.featured .service-link{color:var(--white)}

/* testimonials */
.avatar{position:absolute;border-radius:50%;border:3px solid #e9e9e9}
.quote{position:absolute;left:210px;top:2404px;width:780px;text-align:center;font-size:16px;line-height:1.8;color:var(--text)}
.stars{position:absolute;left:0;width:1200px;top:2506px;text-align:center;color:#f18a16;font-size:20px;letter-spacing:3px}
.reviewer{position:absolute;left:0;width:1200px;top:2536px;text-align:center;font-size:13px;font-weight:600;color:var(--ink)}

/* inquiry */
.field{position:absolute;background:var(--white);border:1px solid #cfe5bb;border-radius:3px;font-size:13px;color:var(--muted);display:flex;align-items:center;gap:8px;padding-left:12px}
.field.message{align-items:flex-start;padding-top:10px}
.submit{position:absolute;left:729px;top:3069px;width:117px;height:36px;background:var(--green);color:var(--white);font-family:'Roboto Slab',serif;font-weight:700;font-size:16px;display:flex;align-items:center;justify-content:center;border-radius:2px}

/* clients */
.client{position:absolute;top:3397px;width:150px;height:150px;border-radius:50%;background:var(--white);box-shadow:0 2px 12px rgba(0,0,0,.08);display:flex;align-items:center;justify-content:center;text-align:center;font-size:16px;font-weight:600;color:var(--ink);line-height:1.2}

/* footer */
.footer-logo .logo-name{font-size:42px}
.footer-col{position:absolute;top:3838px;color:var(--white);font-size:14.5px}
.footer-col h4{font-family:'Roboto Slab',serif;font-weight:700;color:var(--green);font-size:17px;letter-spacing:.5px;margin-bottom:14px}
.footer-col li{list-style:none;margin-bottom:10px}
.footer-col .current{color:var(--yellow);text-decoration:underline}
.contact-line{display:flex;gap:12px;align-items:flex-start;margin-bottom:14px;line-height:1.3}
.bottom-bar{position:absolute;left:0;top:4093px;width:1200px;height:36px;background:var(--lime);color:var(--white);font-size:13px;display:flex;align-items:center;padding-left:88px}
.social{position:absolute;top:4099px;display:flex;gap:10px;left:988px}
.social span{width:24px;height:24px;border-radius:50%;border:2px solid var(--white);display:block}
.social span.on{background:var(--yellow);border-color:var(--yellow)}
</style>
</head>
<body>
<div class="page">

  <!-- HERO -->
  <svg class="abs" style="left:0;top:0" width="1200" height="820" viewBox="0 0 1200 820">
    <defs>
      <linearGradient id="heroGreen" x1="0" y1="0" x2="0" y2="1">
        <stop offset="0" stop-color="#7fcf16"/>
        <stop offset=".55" stop-color="#c6ec8d"/>
        <stop offset="1" stop-color="#ffffff"/>
      </linearGradient>
      <linearGradient id="heroPhoto" x1="0" y1="0" x2="1" y2="1">
        <stop offset="0" stop-color="#3d4d5c"/>
        <stop offset=".45" stop-color="#8fa3b5"/>
        <stop offset=".75" stop-color="#c9d6e4"/>
        <stop offset="1" stop-color="#5a7aa8"/>
      </linearGradient>
    </defs>
    <path d="M0,340 C160,330 300,380 420,500 C540,630 720,710 920,700 C1060,690 1150,650 1200,620 L1200,820 L0,820 Z" fill="url(#heroGreen)"/>
    <path role="img" aria-label="Photo: two businessmen smiling and shaking hands in an office" d="M0,0 H1200 V640 C1120,680 980,700 840,682 C660,655 530,560 430,450 C330,350 180,320 0,352 Z" fill="url(#heroPhoto)"/>
    <path d="M0,352 C180,320 330,350 430,450 C530,560 660,655 840,682 C980,700 1120,680 1200,640" fill="none" stroke="#a5e22c" stroke-width="8"/>
  </svg>

  <div class="logo" style="left:88px;top:36px">
    <span class="logo-mark"></span><span class="logo-name">VELORA</span>
  </div>
  <nav class="nav">
    <span class="active">HOME</span><span>ABOUT US</span><span>SERVICES</span><span>CONTACT US</span>
  </nav>
  <div class="call-btn">
    <svg width="14" height="14" viewBox="0 0 24 24"><path d="M6.6 10.8a15 15 0 0 0 6.6 6.6l2.2-2.2a1 1 0 0 1 1-.25 11.4 11.4 0 0 0 3.6.57 1 1 0 0 1 1 1V20a1 1 0 0 1-1 1A17 17 0 0 1 3 4a1 1 0 0 1 1-1h3.5a1 1 0 0 1 1 1c0 1.25.2 2.45.57 3.57a1 1 0 0 1-.25 1z" fill="#111"/></svg>
    Call Now!
  </div>

  <div class="hero-ring"></div>
  <div class="hero-card">
    <div class="hero-kicker">BUSINESS</div>
    <div class="hero-title">ADVISORS &amp;<br>CONSULTANTS</div>
    <div class="hero-sub">Why Settle for Less When<br>Your Finances Could be<br><span>Exact</span>?</div>
  </div>
  <div class="consult-btn">SHEDULE A<br>FREE CONSULT<br>NOW</div>

  <!-- ABOUT -->
  <div class="section-title" style="left:88px;top:838px;text-align:left">ABOUT US
    <svg width="150" height="12" viewBox="0 0 150 12" style="margin:0"><path d="M2,9 C50,0 100,0 148,6" fill="none" stroke="#5cb833" stroke-width="3"/></svg>
  </div>
  <p class="about-lead">Lorem Ipsum is simply dummy text of the printing and typesetting industry.</p>
  <p class="about-body" style="top:984px">Lorem Ipsum has been the industry's standard dummy text ever since the 1500s, when an unknown printer took a galley of type and scrambled it to make a type specimen book.</p>
  <p class="about-body" style="top:1070px">It has survived not only five centuries, but also the leap into electronic typesetting, remaining essentially unchanged.</p>
  <div class="btn-yellow" style="left:88px;top:1155px;width:137px;height:36px">READ MORE</div>

  <div class="feature" style="left:63px;top:1246px">
    <div class="feature-icon"><svg width="44" height="44" viewBox="0 0 44 44" fill="none" stroke="#fff" stroke-width="2"><circle cx="17" cy="17" r="9"/><circle cx="17" cy="17" r="3"/><circle cx="30" cy="29" r="7"/><path d="M8 40h28"/></svg></div>
    Expirienced
  </div>
  <div class="feature" style="left:261px;top:1246px">
    <div class="feature-icon"><svg width="44" height="44" viewBox="0 0 44 44" fill="none" stroke="#fff" stroke-width="2"><circle cx="22" cy="13" r="5"/><circle cx="11" cy="17" r="4"/><circle cx="33" cy="17" r="4"/><path d="M12 33c0-6 4-10 10-10s10 4 10 10"/><path d="M4 38h36"/></svg></div>
    Professional
  </div>
  <div class="feature" style="left:461px;top:1246px">
    <div class="feature-icon"><svg width="44" height="44" viewBox="0 0 44 44" fill="none" stroke="#fff" stroke-width="2"><circle cx="24" cy="14" r="9"/><path d="M24 9v10M21 12h5a2 2 0 0 1 0 4h-4"/><path d="M4 32h10l8 4 14-6"/></svg></div>
    Affordable
  </div>

  <svg class="abs" style="left:650px;top:812px" width="550" height="580" viewBox="0 0 550 580">
    <defs>
      <linearGradient id="aboutPhoto" x1="0" y1="0" x2="1" y2="1">
        <stop offset="0" stop-color="#6f7f8e"/>
        <stop offset=".5" stop-color="#d9dce2"/>
        <stop offset="1" stop-color="#e9c9cf"/>
      </linearGradient>
    </defs>
    <path d="M305,10 A280,280 0 1 0 330,570" fill="none" stroke="#ffc928" stroke-width="18"/>
    <circle role="img" aria-label="Photo: smiling businesswoman with a colleague working at a laptop" cx="300" cy="290" r="275" fill="url(#aboutPhoto)"/>
  </svg>

  <!-- SERVICES -->
  <svg class="abs" style="left:0;top:1460px" width="1200" height="660" viewBox="0 0 1200 660">
    <path d="M0,90 C200,10 400,0 620,70 C800,120 980,60 1200,70 L1200,560 C1000,620 760,670 560,610 C360,550 150,520 0,540 Z" fill="#dcf0c8"/>
    <path d="M700,80 C850,20 1000,10 1200,60 L1200,130 C1050,90 900,90 700,80 Z" fill="#b9e4a0"/>
    <path d="M0,500 C200,520 400,560 560,610 C380,590 180,560 0,560 Z" fill="#b9e4a0"/>
  </svg>
  <div class="section-title" style="left:400px;width:400px;top:1592px">SERVICES
    <svg width="150" height="12" viewBox="0 0 150 12"><path d="M2,9 C50,0 100,0 148,6" fill="none" stroke="#5cb833" stroke-width="3"/></svg>
  </div>

  <div class="service-card" style="left:88px">
    <svg class="service-icon" viewBox="0 0 70 52"><circle cx="48" cy="26" r="20" fill="#cdebb4"/><rect x="16" y="4" width="26" height="40" fill="none" stroke="#5cb833" stroke-width="2.5"/><path d="M21 14h16M21 22h16M21 30h16M21 38h10" stroke="#5cb833" stroke-width="2.5"/></svg>
    <div class="service-name">Accounting</div>
    <div class="service-list">Bookkeeping<br>Compilations &amp; Reviews<br>Payroll Services</div>
    <div class="service-link">READ MORE</div>
  </div>
  <div class="service-card" style="left:351px">
    <svg class="service-icon" viewBox="0 0 70 52"><circle cx="48" cy="26" r="20" fill="#cdebb4"/><rect x="14" y="4" width="30" height="42" fill="none" stroke="#5cb833" stroke-width="2.5"/><text x="17" y="17" font-family="Poppins,sans-serif" font-size="10" fill="#5cb833">TAX</text><path d="M19 26h20M19 33h20M19 40h12" stroke="#5cb833" stroke-width="2.5"/></svg>
    <div class="service-name">Tax</div>
    <div class="service-list">Individual Tax Preparation<br>Business Tax Preparation<br>Estate &amp; Trust Preparation<br>Audit Representation</div>
    <div class="service-link">READ MORE</div>
  </div>
  <div class="service-card featured" style="left:612px">
    <svg class="service-icon" viewBox="0 0 70 52"><circle cx="48" cy="26" r="20" fill="#ffc928"/><circle cx="22" cy="12" r="6" fill="none" stroke="#fff" stroke-width="2.5"/><path d="M12 44V28a10 10 0 0 1 20 0v16" fill="none" stroke="#fff" stroke-width="2.5"/><path d="M36 14h16v14H36z" fill="none" stroke="#fff" stroke-width="2.5"/></svg>
    <div class="service-name">Consulting</div>
    <div class="service-list">Entity Selection &amp; Restructuring<br>Financial Projections &amp; Forcasts<br>Retirement Planning<br>IPO Readiness</div>
    <div class="service-link" style="text-decoration:underline">READ MORE</div>
  </div>
  <div class="service-card" style="left:875px">
    <svg class="service-icon" viewBox="0 0 70 52"><circle cx="48" cy="26" r="20" fill="#cdebb4"/><rect x="14" y="4" width="28" height="42" fill="none" stroke="#5cb833" stroke-width="2.5"/><path d="M20 14h4M28 14h9M20 24h4M28 24h9M20 34h4M28 34h9" stroke="#5cb833" stroke-width="2.5"/></svg>
    <div class="service-name">Additional Services</div>
    <div class="service-list">CFO Services<br>Compliance Services<br>Controller Services<br>Software Implementations</div>
    <div class="service-link">READ MORE</div>
  </div>

  <!-- TESTIMONIALS -->
  <div class="section-title" style="left:400px;width:400px;top:2198px">TESTIMONIALS
    <svg width="150" height="12" viewBox="0 0 150 12"><path d="M2,9 C50,0 100,0 148,6" fill="none" stroke="#5cb833" stroke-width="3"/></svg>
  </div>
  <svg class="abs" style="left:412px;top:2312px" width="16" height="18" viewBox="0 0 16 18"><path d="M11 2 4 9l7 7" fill="none" stroke="#555" stroke-width="2"/></svg>
  <div class="avatar" role="img" aria-label="Client portrait" style="left:470px;top:2292px;width:58px;height:58px;background:#c9a58a"></div>
  <div class="avatar" role="img" aria-label="Client portrait" style="left:553px;top:2276px;width:92px;height:92px;background:#d7b597;border-color:#ffc928"></div>
  <div class="abs" style="left:585px;top:2352px;width:30px;height:30px;border-radius:50%;background:var(--green);color:#fff;font-family:'Alfa Slab One',serif;font-size:20px;text-align:center;line-height:36px">&#8220;</div>
  <div class="avatar" role="img" aria-label="Client portrait" style="left:670px;top:2292px;width:58px;height:58px;background:#8d6e5a"></div>
  <div class="abs" style="left:768px;top:2310px;width:24px;height:24px;border-radius:50%;background:var(--yellow)"></div>
  <svg class="abs" style="left:774px;top:2315px" width="12" height="14" viewBox="0 0 12 14"><path d="M4 2l5 5-5 5" fill="none" stroke="#333" stroke-width="2"/></svg>

  <p class="quote">Lorem Ipsum is simply dummy text of the printing and typesetting industry. Lorem Ipsum has been the industry's standard dummy text ever since the 1500s, when an unknown printer took a galley of type and scrambled...</p>
  <div class="stars">★★★★★</div>
  <div class="reviewer">Dana Holloway</div>

  <!-- QUICK INQUIRY -->
  <svg class="abs" style="left:0;top:2630px" width="1200" height="620" viewBox="0 0 1200 620">
    <defs>
      <linearGradient id="inqPhoto" x1="0" y1="0" x2="1" y2="1">
        <stop offset="0" stop-color="#f1f3f5"/>
        <stop offset=".5" stop-color="#c9ced4"/>
        <stop offset="1" stop-color="#7d8590"/>
      </linearGradient>
    </defs>
    <path d="M250,60 C450,0 700,-10 900,40 C1020,70 1120,60 1200,40 L1200,560 C1050,620 850,610 650,580 C450,550 300,560 200,570 Z" fill="#dcf0c8"/>
    <path d="M380,575 C500,540 700,560 850,600 C650,600 500,580 380,575 Z" fill="#c8e8ad"/>
    <path d="M-20,60 C100,-5 300,0 420,120" fill="none" stroke="#ffc928" stroke-width="16"/>
    <circle role="img" aria-label="Photo: hand holding a smartphone over a laptop" cx="185" cy="285" r="255" fill="url(#inqPhoto)"/>
  </svg>
  <div class="section-title" style="left:587px;width:400px;top:2806px">QUICK INQUIRY
    <svg width="150" height="12" viewBox="0 0 150 12"><path d="M2,9 C50,0 100,0 148,6" fill="none" stroke="#5cb833" stroke-width="3"/></svg>
  </div>
  <div class="field" style="left:512px;top:2890px;width:267px;height:36px">
    <svg width="13" height="13" viewBox="0 0 24 24" fill="none" stroke="#5cb833" stroke-width="2.5"><circle cx="12" cy="8" r="5"/><path d="M3 22c0-5 4-8 9-8s9 3 9 8"/></svg>Name</div>
  <div class="field" style="left:512px;top:2941px;width:267px;height:36px">
    <svg width="13" height="13" viewBox="0 0 24 24" fill="none" stroke="#5cb833" stroke-width="2.5"><rect x="2" y="5" width="20" height="14"/><path d="M2 5l10 8 10-8"/></svg>Email</div>
  <div class="field" style="left:512px;top:2991px;width:267px;height:36px">
    <svg width="13" height="13" viewBox="0 0 24 24" fill="none" stroke="#5cb833" stroke-width="2.5"><rect x="6" y="2" width="12" height="20" rx="2"/><path d="M10 18h4"/></svg>Phone</div>
  <div class="field message" style="left:796px;top:2890px;width:266px;height:137px">
    <svg width="13" height="13" viewBox="0 0 24 24" fill="none" stroke="#5cb833" stroke-width="2.5"><path d="M4 3h16v14l-6 5H4z"/></svg>Message</div>
  <div class="submit">Submit</div>

  <!-- CLIENTS -->
  <div class="section-title" style="left:400px;width:400px;top:3317px">OUR CLIENTS
    <svg width="150" height="12" viewBox="0 0 150 12"><path d="M2,9 C50,0 100,0 148,6" fill="none" stroke="#5cb833" stroke-width="3"/></svg>
  </div>
  <div class="client" style="left:156px">Vandrel</div>
  <div class="client" style="left:340px">Hollis<br>Marr</div>
  <div class="client" style="left:524px">Burgeo</div>
  <div class="client" style="left:710px">Tamsin<br>Works</div>
  <div class="client" style="left:894px">Kestral<br>Sport</div>

  <!-- FOOTER -->
  <svg class="abs" style="left:0;top:3590px" width="1200" height="510" viewBox="0 0 1200 510">
    <defs>
      <linearGradient id="footGreen" x1="0" y1="0" x2="0" y2="1">
        <stop offset="0" stop-color="#ffffff"/>
        <stop offset=".25" stop-color="#b5e44a"/>
        <stop offset=".55" stop-color="#3f8e12"/>
        <stop offset="1" stop-color="#0e0f0d"/>
      </linearGradient>
      <linearGradient id="mapFill" x1="0" y1="0" x2="1" y2="1">
        <stop offset="0" stop-color="#eef1f4"/>
        <stop offset=".5" stop-color="#e2e8ee"/>
        <stop offset="1" stop-color="#cfdce8"/>
      </linearGradient>
    </defs>
    <rect x="0" y="0" width="1200" height="510" fill="url(#footGreen)"/>
    <path d="M0,160 C300,140 600,200 900,180 C1050,170 1150,150 1200,140 L1200,510 L0,510 Z" fill="#0e0f0d"/>
    <path d="M0,110 C300,90 600,140 900,130 C1050,125 1150,110 1200,100" fill="none" stroke="#a8e033" stroke-width="4" opacity=".8"/>
    <path d="M760,260 A173,173 0 0 1 1000,125" fill="none" stroke="#ffc928" stroke-width="10"/>
    <circle role="img" aria-label="Map showing the office location" cx="913" cy="276" r="170" fill="url(#mapFill)" stroke="#ffffff" stroke-width="4"/>
  </svg>

  <div class="logo footer-logo" style="left:290px;top:3734px">
    <span class="logo-mark" style="width:40px;height:40px"></span><span class="logo-name">VELORA</span>
  </div>

  <div class="footer-col" style="left:88px;width:220px">
    <h4>CONATCT INFO</h4>
    <div class="contact-line"><svg width="14" height="18" viewBox="0 0 14 18"><path d="M7 1a6 6 0 0 1 6 6c0 4-6 10-6 10S1 11 1 7a6 6 0 0 1 6-6z" fill="#5cb833"/><circle cx="7" cy="7" r="2" fill="#0e0f0d"/></svg><span>Lorem ipsum Birchwood<br>ln, Avalon, CA90210</span></div>
    <div class="contact-line"><svg width="14" height="14" viewBox="0 0 24 24"><path d="M6.6 10.8a15 15 0 0 0 6.6 6.6l2.2-2.2a1 1 0 0 1 1-.25 11.4 11.4 0 0 0 3.6.57 1 1 0 0 1 1 1V20a1 1 0 0 1-1 1A17 17 0 0 1 3 4a1 1 0 0 1 1-1h3.5a1 1 0 0 1 1 1c0 1.25.2 2.45.57 3.57a1 1 0 0 1-.25 1z" fill="#5cb833"/></svg><span>(555) 010-4821</span></div>
    <div class="contact-line"><svg width="14" height="14" viewBox="0 0 24 24"><rect x="2" y="8" width="20" height="14" fill="#5cb833"/><rect x="6" y="2" width="12" height="8" fill="none" stroke="#5cb833" stroke-width="2"/></svg><span>(555) 010-7390</span></div>
    <div class="contact-line"><svg width="14" height="14" viewBox="0 0 24 24" fill="none" stroke="#5cb833" stroke-width="2.5"><rect x="2" y="5" width="20" height="14"/><path d="M2 5l10 8 10-8"/></svg><span>nora@velora.com</span></div>
  </div>
  <div class="footer-col" style="left:352px">
    <h4>QUICK LINKS</h4>
    <ul><li class="current">Home</li><li>About Us</li><li>Services</li><li>Contact Us</li></ul>
  </div>
  <div class="footer-col" style="left:545px">
    <h4>SERVICES</h4>
    <ul><li>Accounting</li><li>Tax</li><li>Consulting</li><li>Additional Services</li></ul>
  </div>

  <div class="bottom-bar">© 2023 Velora. All Right Reserved</div>
  <div class="social"><span></span><span class="on"></span><span></span><span></span></div>

</div>
</body>
</html>
```